Tatami Hall Sport promotional leaflet to attract new members

We are looking to produce a leaflet for a local judo club to attract seniors and juniors 5+ the leaflet needs to encourage people to attend classes and train in the martial art

Tatami Hall Sport are proud members of the KSB UK (mats for every) and practice traditional judo which mean we wear white Gi's to show cleanliness and tradition.

www.tatamihallsport.co.uk

Target Market(s)

Kids from 5+ and Adults

Font styles to use
Serif

Requirements
Must have
• Must include times of training and how to book onto a beginners induction
• it must look enticing and show that Judo is fun for all
• must highlight we open on Tuesdays and Thursdays
• Juniors are from 6.15pm to 7.15pm
• seniors 7.30pm to 9pm
• classes are held at Vantrel Gym, Unit 7, Marlow Row, Denholm Close, Rustington, West Sussex, BN17 8QT
• We practice on a Sprung floor Mat area and is great for men and women
• first two classes free
Nice to have
• Classes are run by an expeirnced team including
• Dan Merrow 5th Dan and international referee
• Luke Merrow 2nd Dan current Global Grappling Union European Champion

```html
<!DOCTYPE html>
<html lang="en">
<head>
<meta charset="utf-8">
<title>Tatami Hall Sport – Judo is fun for all</title>
<link rel="stylesheet" href="https://fonts.googleapis.com/css2?family=Zilla+Slab:wght@600;700&family=Crimson+Pro:wght@300;400;500&display=swap">
<style>
  :root {
    --red: #b1202b;
    --navy: #0e1236;
    --white: #ffffff;
    --photo-dark: #2a2d36;
    --photo-light: #8a8d94;
    --bold: "Zilla Slab", Georgia, serif;
    --light: "Crimson Pro", Georgia, serif;
  }
  * { box-sizing: border-box; margin: 0; padding: 0; }
  html, body { width: 927px; height: 1200px; overflow: hidden; background: var(--red); }
  .leaflet { position: relative; width: 927px; height: 1200px; background: var(--red); overflow: hidden; }

  .hero-photo {
    position: absolute; left: 0; top: 0; width: 927px; height: 691px;
    background: radial-gradient(ellipse at 35% 55%, #d9d7d3 0%, var(--photo-light) 35%, var(--photo-dark) 75%);
  }

  .schedule-band {
    position: absolute; left: 0; top: 691px; width: 927px; height: 302px;
    background: var(--navy);
  }
  .open-title {
    position: absolute; left: 0; top: 20px; width: 620px; text-align: center;
    color: var(--white); font-family: var(--bold); font-weight: 700; font-size: 60px; line-height: 1;
  }
  .open-days {
    position: absolute; left: 0; top: 80px; width: 620px; text-align: center;
    color: var(--white); font-family: var(--light); font-weight: 300; font-size: 54px; line-height: 1;
  }
  .times {
    position: absolute; left: 52px; top: 160px; width: 514px; height: 110px;
    border: 2px solid var(--white); display: flex;
  }
  .times .slot { flex: 1; text-align: center; color: var(--white); padding-top: 14px; }
  .times .slot + .slot { border-left: 2px solid var(--white); }
  .slot-name { font-family: var(--bold); font-weight: 700; font-size: 42px; line-height: 1; }
  .slot-time { font-family: var(--light); font-weight: 400; font-size: 31px; line-height: 1; margin-top: 8px; }

  .offer-panel {
    position: absolute; left: 24px; top: 993px; width: 878px; height: 174px;
    background: var(--white);
  }
  .offer-title {
    position: absolute; left: 46px; top: 10px;
    color: var(--red); font-family: var(--bold); font-weight: 700; font-size: 40px; line-height: 1;
  }
  .team {
    position: absolute; left: 48px; top: 58px;
    color: var(--navy); font-family: var(--light); font-weight: 400; font-size: 24px; line-height: 32px;
  }

  .booking {
    position: absolute; left: 24px; top: 1167px; width: 878px; height: 33px;
    display: flex; align-items: center; justify-content: center;
    color: var(--white); font-family: var(--light); font-weight: 500; font-size: 19px;
  }

  .info-column {
    position: absolute; left: 607px; top: 51px; width: 282px; height: 1047px;
    background: var(--red);
  }
  .club-name {
    height: 93px; background: var(--white);
    display: flex; align-items: center; justify-content: center; gap: 8px;
    color: var(--red); font-family: var(--light); font-weight: 500; font-size: 25px;
  }
  .club-name .dot { width: 20px; height: 20px; border-radius: 50%; background: var(--red); }
  .headline {
    text-align: center; color: var(--white); font-family: var(--bold); font-weight: 700;
    font-size: 96px; line-height: 102px; margin-top: 24px;
  }
  .venue {
    position: absolute; left: 0; top: 638px; width: 282px; text-align: center; color: var(--white);
    font-family: var(--bold); font-weight: 600;
  }
  .venue-title { font-size: 48px; line-height: 1; font-weight: 700; }
  .venue-address { font-size: 21px; line-height: 29px; margin-top: 4px; }
  .mat-note {
    position: absolute; left: 0; top: 908px; width: 282px; text-align: center; color: var(--white);
    font-family: var(--bold); font-weight: 600; font-size: 24px; line-height: 29px;
  }
</style>
</head>
<body>
<main class="leaflet">
  <div class="hero-photo" role="img" aria-label="Photo of a black belt coach in a white gi standing with two smiling junior judoka in white gis"></div>

  <section class="schedule-band">
    <h2 class="open-title">WE OPEN ON</h2>
    <p class="open-days">Tuesdays and Thursdays</p>
    <div class="times">
      <div class="slot"><div class="slot-name">JUNIORS</div><div class="slot-time">6.15pm to 7.15pm</div></div>
      <div class="slot"><div class="slot-name">SENIORS</div><div class="slot-time">7.30pm to 9pm</div></div>
    </div>
  </section>

  <section class="offer-panel">
    <h2 class="offer-title">FIRST TWO CLASSES FREE</h2>
    <p class="team">Classes are run by an expeirnced team including<br>
      Dan Merrow 5th Dan and international referee<br>
      Luke Merrow 2nd Dan current Global Grappling Union European Champion</p>
  </section>

  <p class="booking">Book your beginners induction at www.tatamihallsport.co.uk</p>

  <aside class="info-column">
    <div class="club-name"><span class="dot"></span>Tatami Hall Sport</div>
    <h1 class="headline">JUDO<br>IS<br>FUN<br>FOR<br>ALL</h1>
    <div class="venue">
      <div class="venue-title">Classes</div>
      <p class="venue-address">are held at<br>Vantrel Gym, Unit 7,<br>Marlow Row,<br>Denholm Close,<br>Rustington,<br>West Sussex, BN17 8QT</p>
    </div>
    <p class="mat-note">We practice on a<br>Sprung floor Mat<br>area and is great<br>for men and women</p>
  </aside>
</main>
</body>
</html>
```